11 x 17 Orvanthes Quote

Design the following quote in a poster.

"First say to yourself what you would be; then do what you have to do." - Orvanthes

See here for inspiration - https://prints.mornbrekal.com/

Quote

```html
<!DOCTYPE html>
<html lang="en">
<head>
<meta charset="utf-8">
<title>Orvanthes Quote Poster</title>
<link rel="stylesheet" href="https://fonts.googleapis.com/css2?family=Cinzel:wght@400&family=Libre+Baskerville:wght@700&display=swap">
<style>
  :root {
    --paper-light: #f3e9cc;
    --paper-mid: #e3cfa0;
    --paper-edge: #b98a4e;
    --band: #5e0202;
    --ink-light: #ffffff;
    --accent: #f28a1e;
    --attribution: #6a0d0d;
  }
  html, body {
    margin: 0;
    padding: 0;
    overflow: hidden;
  }
  .poster {
    position: relative;
    width: 776px;
    height: 1200px;
    overflow: hidden;
    background:
      radial-gradient(ellipse 75% 65% at 50% 45%, var(--paper-light) 0%, var(--paper-mid) 60%, var(--paper-edge) 100%);
  }
  .quote {
    margin: 0;
  }
  .quote-line {
    position: absolute;
    height: 77px;
    background: var(--band);
    color: var(--ink-light);
    font-family: "Cinzel", serif;
    font-weight: 400;
    font-size: 60px;
    line-height: 80px;
    text-align: center;
    white-space: nowrap;
  }
  .quote-accent {
    color: var(--accent);
  }
  .line-1 { left: 260px; width: 266px; top: 288px; }
  .line-2 { left: 62px;  width: 662px; top: 372px; }
  .line-3 { left: 157px; width: 472px; top: 455px; }
  .line-4 { left: 157px; width: 472px; top: 538px; }
  .line-5 { left: 187px; width: 410px; top: 621px; }
  .line-6 { left: 157px; width: 472px; top: 704px; }
  .line-7 { left: 107px; width: 556px; top: 787px; }
  .attribution {
    position: absolute;
    left: 0;
    width: 776px;
    top: 918px;
    margin: 0;
    text-align: center;
    font-family: "Libre Baskerville", serif;
    font-weight: 700;
    font-size: 25px;
    color: var(--attribution);
  }
</style>
</head>
<body>
<main class="poster">
  <blockquote class="quote">
    <span class="quote-line line-1">"FIRST</span>
    <span class="quote-line line-2">SAY TO <span class="quote-accent">YOURSELF</span></span>
    <span class="quote-line line-3">WHAT YOU</span>
    <span class="quote-line line-4">WOULD BE;</span>
    <span class="quote-line line-5">THEN DO</span>
    <span class="quote-line line-6">WHAT YOU</span>
    <span class="quote-line line-7">HAVE TO DO."</span>
  </blockquote>
  <p class="attribution">Orvanthes</p>
</main>
</body>
</html>
```